Tech business card design

We need an amazing business card design for our new business 'Brakka' a marketing tech startup based in Sydney, Australia. We provide an online marketplace for businesses to search and buy advertising media, connect with service providers and learn more about marketing. We wish to communicate 'cool tech', reliability and professionalism and design based around our logo.

Target Market(s)

Business Owners

Contact Information for Business Card

Name
Position
Email Address
Website
Phone Number

Font styles to use
Other font styles liked:
• Avenir & Avenir Next

Colors

Designer to choose colors to be used in the design.

```html
<!DOCTYPE html>
<html lang="en">
<head>
<meta charset="utf-8">
<title>Brakka business card</title>
<link rel="stylesheet" href="https://fonts.googleapis.com/css2?family=Nunito+Sans:wght@400;800;900&display=swap">
<style>
  :root {
    --navy: #1f1d5a;
    --white: #ffffff;
    --ink: #111111;
    --ink-soft: #333333;
    --network: #e6e6e9;
    --network-light: #f4f4f6;
    --stage: #2c2d30;
  }
  * { margin: 0; padding: 0; box-sizing: border-box; }
  html, body {
    width: 1200px; height: 900px; overflow: hidden;
    background: var(--stage);
    font-family: "Nunito Sans", sans-serif;
  }
  .sheet {
    width: 1200px; height: 900px;
    display: flex; align-items: center; justify-content: center; gap: 40px;
  }
  .card {
    position: relative;
    width: 540px; height: 310px;
    background: var(--white);
    overflow: hidden;
    box-shadow: 0 10px 30px rgba(0,0,0,.45);
  }
  .network-field {
    position: absolute;
    background: radial-gradient(ellipse at center, var(--network) 0%, var(--network-light) 55%, rgba(255,255,255,0) 75%);
  }
  /* back */
  .card-back .brand-band {
    position: absolute; left: 0; top: 0; bottom: 0; width: 170px;
    background: var(--navy);
  }
  .card-back .brand-name {
    position: absolute; left: 85px; top: 155px;
    transform: translate(-50%, -50%) rotate(-90deg);
    color: var(--white);
    font-weight: 900; font-size: 72px; letter-spacing: 1px;
    line-height: 1;
  }
  .card-back .network-field { left: 200px; top: 30px; width: 320px; height: 260px; }
  .person {
    position: absolute; right: 30px; top: 34px; text-align: right;
  }
  .person-name {
    font-weight: 900; font-size: 26px; color: var(--ink); letter-spacing: .5px; line-height: 1;
  }
  .person-role {
    font-weight: 400; font-size: 14px; color: var(--ink-soft); margin-top: 4px;
  }
  .accent-tab {
    position: absolute; right: 0; top: 30px; width: 10px; height: 56px;
    background: var(--navy);
  }
  .contact-list { position: absolute; left: 0; top: 150px; list-style: none; }
  .contact-item {
    position: relative; display: flex; align-items: center;
    height: 40px; padding-left: 158px;
  }
  .contact-item::before {
    content: ""; position: absolute; left: 120px; top: 50%;
    width: 38px; height: 2px; background: var(--white);
  }
  .contact-icon {
    width: 26px; height: 26px; border-radius: 50%;
    background: var(--navy); border: 2px solid var(--white);
    box-shadow: 0 0 0 1px var(--navy);
    display: flex; align-items: center; justify-content: center;
    flex: none;
  }
  .contact-text { margin-left: 12px; font-size: 15px; color: var(--ink); }
  /* front */
  .card-front .network-field { left: 40px; top: 20px; width: 470px; height: 270px; }
  .card-front .brand-name {
    position: absolute; inset: 0;
    display: flex; align-items: center; justify-content: center;
    color: var(--navy); font-weight: 900; font-size: 130px; letter-spacing: 2px;
  }
</style>
</head>
<body>
<main class="sheet">
  <section class="card card-back" aria-label="Card back">
    <div class="network-field" role="img" aria-label="Faint world map made of connected network dots"></div>
    <div class="brand-band"></div>
    <div class="brand-name">Brakka</div>
    <div class="accent-tab"></div>
    <div class="person">
      <div class="person-name">DANA WHITLOCK</div>
      <div class="person-role">Founder, Director</div>
    </div>
    <ul class="contact-list">
      <li class="contact-item">
        <span class="contact-icon">
          <svg width="14" height="14" viewBox="0 0 24 24"><path fill="#fff" d="M6.6 10.8a15 15 0 0 0 6.6 6.6l2.2-2.2c.3-.3.7-.4 1-.2 1.1.4 2.3.6 3.6.6.6 0 1 .4 1 1V20c0 .6-.4 1-1 1A17 17 0 0 1 3 4c0-.6.4-1 1-1h3.5c.6 0 1 .4 1 1 0 1.3.2 2.5.6 3.6.1.3 0 .7-.2 1z"/></svg>
        </span>
        <span class="contact-text">+61 (0)400 555 218</span>
      </li>
      <li class="contact-item">
        <span class="contact-icon">
          <svg width="14" height="14" viewBox="0 0 24 24"><rect x="3" y="6" width="18" height="12" fill="none" stroke="#fff" stroke-width="2"/><path d="M3 6l9 7 9-7" fill="none" stroke="#fff" stroke-width="2"/></svg>
        </span>
        <span class="contact-text">dana@brakkamedia.com.au</span>
      </li>
      <li class="contact-item">
        <span class="contact-icon">
          <svg width="14" height="14" viewBox="0 0 24 24" fill="none" stroke="#fff" stroke-width="2"><circle cx="12" cy="12" r="9"/><ellipse cx="12" cy="12" rx="4" ry="9"/><path d="M3 12h18"/></svg>
        </span>
        <span class="contact-text">www.brakkamedia.com.au</span>
      </li>
    </ul>
  </section>

  <section class="card card-front" aria-label="Card front">
    <div class="network-field" role="img" aria-label="Faint world map made of connected network dots"></div>
    <div class="brand-name">Brakka</div>
  </section>
</main>
</body>
</html>
```